Packaging Design for Boneless Picnic Ham

We are Bright Larder Limited, a company based in Trinidad which is located within the Caribbean. We produce and sell a plethora of meat products including a variety of hams, sausages and even bacon.

We require a packaging design for a ham product. This product is packaged within a cryovac (11" X 18") shrink bag which would be used to package our Boneless Picnic Ham which weighs 2.5 Kilograms.

The design space should be 7 inches wide and 6 inches in height. The design is 3 inches from the bottom and 2 inches off each side.

Our target audience comprises of caterers as well as the average household folk. What sets our product apart is that it is has a great taste, 20% less salt and is affordable and easy. We commonly refer to it as the "Oven Ready Roast".

Attached below, is our logo which you must incorporate onto the design. We also request that the header be "Applewood Cured Rolled Country Pork".

Target Market(s)

Caterers and Average Household Folk

Industry/Entity Type

It Company

Font styles to use
Sans Serif

Requirements
Must have
• The Bright Larder Company Logo and the header must have "Applewood Cured Rolled Country Pork"
Nice to have
• Maximum Creativity
Should not have
• No animal artwork should be included onto the design

```html
<!DOCTYPE html>
<html lang="en">
<head>
<meta charset="utf-8">
<title>Bright Larder – Applewood Cured Rolled Country Pork Label</title>
<link rel="stylesheet" href="https://fonts.googleapis.com/css2?family=Oswald:wght@600&family=Open+Sans:wght@400;600;700;800&display=swap">
<style>
  :root {
    --page: #ebebeb;
    --label-top: #eef2f8;
    --brand-red: #e01e3a;
    --brand-navy: #2a3590;
    --white: #ffffff;
    --ink: #1a1a1a;
    --muted: #777777;
  }
  * { box-sizing: border-box; margin: 0; padding: 0; }
  html, body { width: 1200px; height: 1000px; overflow: hidden; background: var(--page); }
  .canvas { position: relative; width: 1200px; height: 1000px; }

  .label {
    position: absolute; left: 69px; top: 45px; width: 1064px; height: 910px;
    border-radius: 20px; overflow: hidden; background: var(--brand-red);
    box-shadow: 0 2px 14px rgba(0,0,0,0.12);
  }
  .label-header {
    position: absolute; left: 0; top: 0; width: 100%; height: 252px;
    background: var(--label-top);
  }
  .brand {
    position: absolute; left: 0; top: 80px; width: 1032px;
    display: flex; align-items: center; justify-content: center; gap: 16px;
  }
  .brand-dot { width: 34px; height: 34px; border-radius: 50%; background: var(--brand-navy); }
  .brand-name {
    font-family: "Open Sans", sans-serif; font-weight: 800; font-size: 50px;
    color: var(--brand-navy); letter-spacing: -0.5px;
  }
  .net-weight {
    position: absolute; right: 34px; top: 152px;
    font-family: "Open Sans", sans-serif; font-weight: 400; font-size: 60px;
    color: var(--brand-red); line-height: 1;
  }

  .product-title {
    position: absolute; left: 0; top: 282px; width: 100%;
    font-family: "Oswald", sans-serif; font-weight: 600; font-size: 112px;
    line-height: 126px; color: var(--label-top); text-align: center;
    text-transform: uppercase; white-space: nowrap; letter-spacing: -0.5px;
  }

  .description {
    position: absolute; left: 36px; top: 570px; width: 594px;
    font-family: "Open Sans", sans-serif; font-weight: 600; color: var(--white);
    text-align: justify;
  }
  .description p { font-size: 11.2px; line-height: 13.6px; margin-bottom: 7px; }
  .description p.closing { font-size: 12.4px; line-height: 15px; margin-top: 16px; font-weight: 400; }

  .nutrition {
    position: absolute; left: 656px; top: 572px; width: 367px; height: 175px;
    background: var(--white); color: var(--ink); display: flex; padding: 6px 8px;
    font-family: "Open Sans", sans-serif; gap: 10px;
  }
  .nutrition-intro { width: 158px; font-size: 8px; line-height: 10px; }
  .nutrition-title { font-weight: 800; font-size: 24px; line-height: 31px; margin-bottom: 2px; }
  .nutrition-intro .calories { font-weight: 700; }
  .nutrition-intro .note { font-size: 6px; line-height: 7.5px; margin-top: 2px; }
  .nutrition-table { flex: 1; font-size: 8.5px; }
  .nutrition-table .row {
    display: flex; justify-content: space-between; border-bottom: 1px solid #999;
    padding: 2px 0; line-height: 11px;
  }
  .nutrition-table .row.head { font-size: 6px; border-bottom: 4px solid var(--ink); }
  .nutrition-table .row.thick { border-bottom: 4px solid var(--ink); }
  .nutrition-table .row.sub { padding-left: 12px; }
  .nutrition-table b { font-weight: 700; }
  .nutrition-table .footnote { font-size: 5.5px; line-height: 7px; color: #444; margin-top: 3px; }

  .claim-serve {
    position: absolute; left: 656px; top: 765px; width: 370px; text-align: center;
    font-family: "Open Sans", sans-serif; font-weight: 800; font-size: 39px;
    color: var(--label-top); line-height: 1;
  }
  .claim-salt {
    position: absolute; left: 656px; top: 832px; width: 370px; text-align: center;
    font-family: "Open Sans", sans-serif; font-weight: 800; font-size: 23px;
    color: var(--label-top); letter-spacing: 5px; line-height: 1;
  }
</style>
</head>
<body>
<div class="canvas">
  <div class="label">
    <div class="label-header">
      <div class="brand">
        <span class="brand-dot"></span>
        <span class="brand-name">Bright Larder</span>
      </div>
      <div class="net-weight">700 g</div>
    </div>

    <h1 class="product-title">Applewood Cured<br>Rolled Country Pork</h1>

    <div class="description">
      <p>Lorem ipsum dolor sit amet, consectetur adipisicing elit, sed do eiusmod tempor incididunt ut labore et dolore magna aliqua. Ut enim ad minim veniam, quis nostrud exercitation. Lorem ipsum dolor sit amet, consectetur adipisicing elit, sed do eiusmod tempor incididunt ut labore et dolore magna aliqua. Ut enim ad minim veniam, quis nostrud exercitation. Lorem ipsum dolor sit amet, consectetur adipisicing elit, sed do eiusmod tempor incididunt ut labore et dolore magna aliqua. Ut enim ad minim veniam, quis nostrud exercitation.</p>
      <p>Lorem ipsum dolor sit amet, consectetur adipisicing elit, sed do eiusmod tempor incididunt ut labore et dolore magna aliqua. Ut enim ad minim veniam, quis nostrud exercitation. Lorem ipsum dolor sit amet, consectetur adipisicing elit, sed do eiusmod tempor incididunt ut labore et dolore magna aliqua. Ut enim ad minim veniam, quis nostrud exercitation. Lorem ipsum dolor sit amet, consectetur adipisicing elit, sed do eiusmod tempor incididunt ut labore et dolore magna aliqua. Ut enim ad minim veniam, quis nostrud exercitation. Lorem ipsum dolor sit amet, consectetur adipisicing elit, sed do eiusmod tempor incididunt ut labore et dolore magna aliqua. Ut enim ad minim veniam, quis nostrud exercitation. Lorem ipsum dolor sit amet, consectetur adipisicing elit, sed do eiusmod tempor incididunt ut labore et dolore magna aliqua. Ut enim ad minim veniam, quis nostrud exercitation. Lorem ipsum dolor sit amet, consectetur adipisicing elit, sed do eiusmod tempor incididunt ut labore et dolore magna aliqua. Ut enim ad minim veniam, quis nostrud exercitation.</p>
      <p class="closing">Lorem ipsum dolor sit amet, consectetur adipisicing elit, sed do eiusmod tempor incididunt ut labore et dolore magna aliqua. Ut enim ad minim veniam, quis nostrud exercitation. Lorem ipsum dolor sit amet, consectetur adipisicing elit.</p>
    </div>

    <div class="nutrition">
      <div class="nutrition-intro">
        <div class="nutrition-title">Nutrition<br>Facts</div>
        <div>Serving Size 1 tbsp. (20g)</div>
        <div>Servings Per Container 18</div>
        <div class="calories">Calories 50</div>
        <div class="note">*Percent Daily Values are based on a 2,000 calorie diet.</div>
      </div>
      <div class="nutrition-table">
        <div class="row head"><span>Amount / Serving</span><span>% Daily Value*</span></div>
        <div class="row"><span><b>Total Fat</b> 0g</span><b>0%</b></div>
        <div class="row"><span><b>Sodium</b> 0mg</span><b>0%</b></div>
        <div class="row"><span><b>Total Carbohydrate</b> 13g</span><b>4%</b></div>
        <div class="row sub"><span>Sugars 13g</span><span></span></div>
        <div class="row thick"><span><b>Protein</b> 0g</span><span></span></div>
        <div class="row"><span>Vitamin C 2%</span><span></span></div>
        <div class="footnote">Not a significant source of calories from fat, saturated fat, trans fat, cholesterol, dietary fiber, vitamin A, calcium and iron.</div>
      </div>
    </div>

    <div class="claim-serve">READY TO SERVE</div>
    <div class="claim-salt">20% LESS SALT</div>
  </div>
</div>
</body>
</html>
```